website update

We need to redesign our current website to be more personalised and sophisticated. We are physiotherapy clinic based in sydney australia, offer a range of clinical service such as Physiotherapy, Massage, sports injuries rehabilitation, Women's health (incontinency etc), Pilates classes, back pain exercise program, acupuncture, Gait analysis.
our current website is www.bluegumrehab.com.au
an example of ideal website is http://corvellabodyworks.com/
homepage: with a revolving displaying attached photos which is linked to relevants page

```html
<!DOCTYPE html>
<html lang="en">
<head>
<meta charset="utf-8">
<title>Bluegum Rehab – Physiotherapy &amp; Sports Clinic</title>
<link rel="stylesheet" href="https://fonts.googleapis.com/css2?family=Source+Sans+3:ital,wght@0,400;0,600;0,700;1,400;1,600&display=swap">
<style>
:root{
  --green:#9dc93a;
  --green-dark:#6fa52a;
  --cream:#eef0cf;
  --topbar:#f1f3d6;
  --ink:#1d1d1d;
  --muted:#7a7a7a;
  --footer:#2e2e2e;
  --white:#ffffff;
}
*{box-sizing:border-box;margin:0;padding:0}
html,body{width:853px;height:1200px;overflow:hidden;background:var(--white)}
body{position:relative;font-family:"Source Sans 3",Arial,sans-serif;color:var(--ink)}
.abs{position:absolute}
ul{list-style:none}

.topbar{left:0;top:0;width:853px;height:30px;background:var(--topbar)}
.topbar-email{left:450px;top:9px;font-size:9px;font-weight:600;color:var(--green-dark);display:flex;align-items:center;gap:6px}
.social{display:flex;gap:4px}
.social span{width:21px;height:21px;background:#e9e9e9;border:1px solid #cfcfcf;border-radius:3px;display:block;position:relative}
.social span::after{content:"";position:absolute;left:7px;top:7px;width:6px;height:6px;border-radius:50%;background:#888}
.social span.on{background:var(--green)}
.social span.on::after{background:var(--white)}
.topbar-social{left:645px;top:3px}

.brand{left:78px;top:43px;display:flex;align-items:center;gap:10px}
.brand-dot{width:52px;height:52px;border-radius:50%;background:var(--green)}
.brand-name{font-size:24px;font-weight:700;color:var(--green-dark);line-height:1}
.brand-sub{font-size:9px;color:#555;letter-spacing:.3px;margin-top:3px}

.contact-head{right:100px;top:36px;text-align:right;font-size:8.5px;line-height:12.8px;color:var(--muted);font-weight:600}
.phone{font-size:18px;font-weight:400;color:var(--green);display:flex;align-items:center;justify-content:flex-end;gap:6px;line-height:22px;margin-bottom:1px}
.phone svg{width:20px;height:20px}

.hero{left:0;top:142px;width:853px;height:325px;background:linear-gradient(100deg,#f1e4d6 0%,#efcfae 35%,#f0ae7c 60%,#e88d5a 80%,#c86e48 100%)}
.tagline{left:514px;top:238px;font-style:italic;font-size:26px;line-height:31px;color:#111}
.tagline span{display:block}
.tagline .l1{font-weight:600}
.tagline .l2{padding-left:42px;font-weight:400}
.tagline .l3{padding-left:47px;font-weight:600}
.tagline .l4{padding-left:97px;font-weight:400}
.hero-arrows{left:696px;top:426px}

.nav{left:74px;top:116px;width:706px;height:51px;background:var(--green);border-radius:2px;display:flex;align-items:center;padding-left:29px}
.nav a{color:var(--white);font-size:12px;font-weight:600;text-decoration:none;margin-right:14px;white-space:nowrap}

.welcome{left:70px;top:406px;width:420px;height:379px;background:var(--cream);padding:16px 22px 0 20px}
.welcome h1{font-size:17px;font-weight:400;padding-bottom:6px;border-bottom:1px solid #d6d8b4;margin-bottom:8px}
.welcome p{font-size:8.9px;line-height:17px;text-align:justify}
.read-more{font-size:8.5px;color:var(--green-dark);text-align:right;padding-right:8px}
.welcome h2{font-size:12px;font-style:italic;font-weight:400;line-height:15px;margin:8px 0 12px}
.arrow-list li{font-size:10px;line-height:17px;color:#444;padding-left:18px;position:relative}
.arrow-list li::before{content:"\2192";position:absolute;left:4px;top:0;font-size:8px}

.video{left:506px;top:476px;width:275px;height:176px;background:#eee;border:1px solid #ddd;padding:4px}
.video-still{width:100%;height:100%;background:linear-gradient(90deg,#e8e8e8,#d6c4b8 55%,#9b8a7e)}
.play{left:126px;top:62px}
.partners{left:506px;top:660px;width:275px;height:125px;border:1px solid #e3e3e3;display:grid;grid-template-columns:repeat(4,1fr);gap:10px 8px;padding:14px 10px}
.partners span{height:24px;background:#e4e4e4;border-radius:2px}
.partners span.wide{grid-column:span 2;height:46px;border-radius:4px}

.conditions-title{left:90px;top:798px;font-size:17px;font-weight:400}
.cond-col{top:836px;width:130px}
.cond-col h3{font-size:12px;font-weight:400;margin-bottom:12px}
.cond-col h3 small{font-size:8.5px}
.cond-col li{font-size:9px;line-height:17px;padding-left:10px;position:relative}
.cond-col li::before{content:"\2192";position:absolute;left:0;font-size:7px}
.thumb{top:1000px;width:126px;height:81px;background:#f2f2f2;border:1px solid #e2e2e2;padding:4px}
.thumb div{width:100%;height:100%}

.talk{left:533px;top:802px;width:206px;height:88px;background:var(--green);padding:10px 12px;color:var(--white)}
.talk h3,.appt h3{font-size:15px;font-weight:400;margin-bottom:6px}
.talk p{font-size:8.5px;line-height:12px;color:#f4f9e6}
.talk-tail{left:554px;top:889px}
.appt{left:533px;top:910px;width:206px;height:102px;background:var(--green);padding:7px 12px;color:var(--white)}
.appt h3{border-bottom:1px solid #b8db72;padding-bottom:3px;margin-bottom:9px}
.appt li{font-size:8.5px;line-height:17px;padding-left:12px;position:relative}
.appt li::before{content:"";position:absolute;left:2px;top:7px;width:4px;height:4px;border-radius:50%;background:var(--white)}
.community{left:533px;top:1016px;width:206px;height:61px;background:linear-gradient(#4a6aa0,#2f4d82);color:var(--white);display:flex;align-items:center;gap:10px;padding-left:14px}
.community i{width:30px;height:30px;background:#e9eef6;border-radius:4px;display:block}
.community b{font-size:15px;line-height:18px;font-weight:700}
.follow{left:533px;top:1081px;font-size:7px;color:#333;display:flex;gap:6px;align-items:center}
.follow span{border:1px solid #ccc;background:#f4f4f4;padding:1px 4px}

.footer{left:0;top:1100px;width:853px;height:100px;background:var(--footer);color:var(--white)}
.footer-nav{left:0;top:16px;width:853px;text-align:center;font-size:8.5px;font-weight:600}
.footer-social{left:375px;top:43px}
.copyright{left:0;top:80px;width:853px;text-align:center;font-size:8.5px;color:#ddd}
</style>
</head>
<body>

<header>
  <div class="abs topbar"></div>
  <div class="abs topbar-email">
    <svg width="16" height="11" viewBox="0 0 16 11"><rect x="0.5" y="0.5" width="15" height="10" fill="#9dc93a"/><path d="M1 1 L8 6 L15 1" stroke="#fff" fill="none"/></svg>
    email: info@bluegumrehab.com.au
  </div>
  <div class="abs social topbar-social" aria-label="Social links"><span class="on"></span><span></span><span></span><span></span></div>

  <div class="abs brand">
    <span class="brand-dot"></span>
    <div>
      <div class="brand-name">bluegum rehab</div>
      <div class="brand-sub">PHYSIOTHERAPY &amp; SPORTS CLINIC</div>
    </div>
  </div>

  <div class="abs contact-head">
    <div class="phone">
      <svg viewBox="0 0 20 20"><circle cx="10" cy="10" r="10" fill="#e8f0c8"/><path d="M6 5c1-1 2 0 3 2s0 2-1 2c0 2 2 4 4 4 0-1 0-2 2-1s3 2 2 3c-1 2-3 2-6 0s-5-5-5-7 0-2 1-3z" fill="#9dc93a"/></svg>
      1800 . 402 .7716
    </div>
    Shop 3, The Arcade,<br>
    112 Laurel St, Northvale 2067 &nbsp;[See a map]<br>
    Shop 5, 20-24 Wattle Rd Eastfield<br>
    2112 Australia &nbsp;[See a map]
  </div>
</header>

<section>
  <div class="abs hero" role="img" aria-label="Slideshow photo of a young woman out running against a warm sunset sky"></div>
  <div class="abs tagline">
    <span class="l1">Get Well</span>
    <span class="l2">Move Well</span>
    <span class="l3">Enjoy the</span>
    <span class="l4">Freedom Again</span>
  </div>
  <svg class="abs hero-arrows" width="38" height="28" viewBox="0 0 38 28"><path d="M14 2 L3 14 L14 26 M24 2 L35 14 L24 26" stroke="#fff" stroke-width="2" fill="none"/></svg>
</section>

<nav class="abs nav">
  <a>Home</a><a>About us</a><a style="margin-left:-8px;margin-right:24px">Common conditions</a><a style="margin-right:18px">Treatments</a><a style="margin-right:3px">Specialised services</a><a style="margin-right:23px">OH&amp;S / Workplace Assessment</a><a>Contact Us</a>
</nav>

<main>
  <article class="abs welcome">
    <h1>Welcome To Our Website</h1>
    <p><b>At Bluegum Rehab Physiotherapy Clinic</b> we believe that effective treatments come with accurate diagnosis. In the clinic we have the latest clinically-proven equipments which will improve the accuracy in the diagnosis of your conditions and pain. We offer in-house assessment services include the use of real-time ultrasound device(to assess muscle weakness &amp; soft-tissue injuries), computerised posture/spinal assessment, computer analysis for walking and running, and computerised foot assessment. Special Services</p>
    <div class="read-more">Read more</div>
    <h2>We are physiotherapy clinic based in sydney australia, offer a range of clinical service such as</h2>
    <ul class="arrow-list">
      <li>Physiotherapy,</li>
      <li>Massage,</li>
      <li>Sports injuries rehabilitation,</li>
      <li>Women's health<br>(incontinency etc),</li>
      <li>Pilates classes,</li>
      <li>Back pain exercise program,</li>
      <li>Acupuncture,</li>
      <li>Gait analysis.</li>
    </ul>
  </article>

  <div class="abs video">
    <div class="video-still" role="img" aria-label="Video still of a physiotherapist guiding a patient through a resistance band exercise"></div>
    <svg class="abs play" width="42" height="42" viewBox="0 0 42 42"><circle cx="21" cy="21" r="21" fill="rgba(40,40,40,.75)"/><path d="M16 12 L30 21 L16 30z" fill="#fff"/></svg>
  </div>

  <div class="abs partners" aria-label="Health fund and association partners">
    <span></span><span></span><span></span><span></span>
    <span class="wide"></span><span class="wide"></span>
  </div>

  <h2 class="abs conditions-title">Common conditions</h2>
  <div class="abs cond-col" style="left:91px">
    <h3>Spinal conditions</h3>
    <ul><li>Back /neck pain, headaches</li><li>Disc bulge/protrusion</li><li>Unstable pelvis or spine</li><li>Nerve impingement</li></ul>
  </div>
  <div class="abs cond-col" style="left:231px">
    <h3>Sports injuries</h3>
    <ul><li>ACL rehab</li><li>Post-op rehab (e.g ACL/meniscal knee recon, shoulder recon)</li><li>Muscle strain/tear</li><li>Rotator cuff</li><li>Sports related back pain</li></ul>
  </div>
  <div class="abs cond-col" style="left:371px;width:128px">
    <h3>RSI <small>(repetitive strain injuries)</small></h3>
    <ul><li>Tennis elbow (lateral epicondylagia)</li><li>Muscle strain</li><li>Achilles tendonosis</li><li>Rotator cuff tendonosis</li></ul>
  </div>
  <div class="abs thumb" style="left:90px"><div role="img" aria-label="Spine model being examined" style="background:linear-gradient(90deg,#6b6259,#cfc7bd 55%,#8a7a62)"></div></div>
  <div class="abs thumb" style="left:230px"><div role="img" aria-label="Athlete being assessed on a treadmill" style="background:linear-gradient(90deg,#9a9a9a,#6e6e6e 50%,#c6c6c6)"></div></div>
  <div class="abs thumb" style="left:372px"><div role="img" aria-label="Patient receiving arm treatment" style="background:linear-gradient(90deg,#e7e2dd,#c9a996 45%,#dfe3e8)"></div></div>

  <aside>
    <div class="abs talk">
      <h3>Talk To Us</h3>
      <p>We are always happy to answer any questions you may have. Email us: info@bluegumrehab.com.au</p>
    </div>
    <svg class="abs talk-tail" width="18" height="14" viewBox="0 0 18 14"><path d="M0 0 H18 L2 14z" fill="#9dc93a"/></svg>
    <div class="abs appt">
      <h3>For Appointments:</h3>
      <ul><li>Eastfield: 02 9351 2208</li><li>Northvale : 02 9417 6630</li><li>Contact us</li></ul>
    </div>
    <div class="abs community"><i></i><b>Join our Community<br>today!</b></div>
    <div class="abs follow"><span>Follow</span>1,223 people like this.</div>
  </aside>
</main>

<footer class="abs footer">
  <div class="abs footer-nav">Home &nbsp;-&nbsp; About us &nbsp;-&nbsp; Common conditions &nbsp;-&nbsp; Treatments &nbsp;-&nbsp; Specialised services &nbsp;-&nbsp; OH&amp;S / Workplace Assessment &nbsp;-&nbsp; Contact Us</div>
  <div class="abs social footer-social"><span class="on"></span><span></span><span></span><span></span></div>
  <div class="abs copyright">© 2014.www.bluegumrehab.com.au</div>
</footer>

</body>
</html>
```